Lantern Hill Publicity is a new boutique Press Office with a small roster of well-chosen clients across an array of disciplines; from Art and Technology to Restaurants and Fashion. Based in Greenpoint Brooklyn, Lantern Hill Publicity achieves outstanding results through hard work, tenacity, efficiency and a sense of humor. We need a simple, versatile and classic design. We would like each side of the card to be white text on a black background.

Boutique

```html
<!DOCTYPE html>
<html lang="en">
<head>
<meta charset="utf-8">
<title>Lantern Hill Publicity — Business Card</title>
<link href="https://fonts.googleapis.com/css2?family=Playfair+Display:wght@600;700&family=Montserrat:wght@400;600&display=swap" rel="stylesheet">
<style>
  :root {
    --card-black: #0b0b0b;
    --paper: #ffffff;
    --backdrop: #e9e9e9;
    --rule: #f2f2f2;
    --faint: #1c1c1c;
    --text-soft: #e6e6e6;
  }
  * { margin: 0; padding: 0; box-sizing: border-box; }
  html, body {
    width: 1200px; height: 900px; overflow: hidden;
    background: var(--backdrop);
  }
  .stage {
    width: 1200px; height: 900px;
    display: flex; flex-direction: column;
    align-items: center; justify-content: center; gap: 40px;
  }
  .card {
    position: relative;
    width: 640px; height: 366px;
    border-radius: 22px;
    overflow: hidden;
    background: var(--card-black);
    color: var(--paper);
    box-shadow: 0 6px 18px rgba(0,0,0,0.18);
  }
  /* Front */
  .front-name {
    position: absolute; left: 0; right: 0; top: 120px;
    text-align: center;
    font-family: "Playfair Display", serif;
    font-weight: 700;
    font-size: 44px;
    letter-spacing: 1px;
  }
  .front-url {
    position: absolute; left: 0; right: 0; bottom: 64px;
    text-align: center;
    font-family: "Montserrat", sans-serif;
    font-weight: 600;
    font-size: 17px;
    letter-spacing: 0.5px;
  }
  /* Back */
  .back-accent {
    position: absolute; right: -70px; top: -20px;
    width: 260px; height: 260px;
    border-radius: 50%;
    background: var(--faint);
  }
  .brand {
    position: absolute; left: 40px; top: 66px;
    font-family: "Playfair Display", serif;
    font-weight: 600;
    text-transform: uppercase;
    font-size: 23px;
    line-height: 1.25;
    letter-spacing: 3px;
  }
  .person {
    position: absolute; left: 360px; right: 0; top: 62px;
    text-align: right;
  }
  .person-name {
    font-family: "Playfair Display", serif;
    font-weight: 600;
    font-size: 20px;
    letter-spacing: 1.5px;
    text-transform: uppercase;
    padding: 0 32px 5px 0;
    border-bottom: 1.5px solid var(--rule);
  }
  .person-role {
    font-family: "Montserrat", sans-serif;
    font-size: 12px;
    padding: 6px 32px 0 0;
    letter-spacing: 0.5px;
    color: var(--text-soft);
  }
  .divider {
    position: absolute; left: 0; top: 170px;
    width: 640px; height: 1.5px;
    background: var(--rule);
  }
  .contact {
    position: absolute; left: 40px; top: 188px;
    font-family: "Montserrat", sans-serif;
    font-size: 14.5px;
    color: var(--text-soft);
    line-height: 1.55;
    list-style: none;
  }
  .contact li { display: flex; align-items: center; gap: 10px; }
  .contact svg { width: 12px; height: 12px; flex: none; }
</style>
</head>
<body>
<main class="stage">
  <section class="card card-front" aria-label="Card front">
    <p class="front-name">Lantern Hill Publicity</p>
    <p class="front-url">www.lanternhill.com</p>
  </section>

  <section class="card card-back" aria-label="Card back">
    <div class="back-accent" aria-hidden="true"></div>
    <p class="brand">Lantern Hill<br>Publicity</p>
    <div class="person">
      <p class="person-name">Mara Ellison</p>
      <p class="person-role">Director</p>
    </div>
    <div class="divider"></div>
    <ul class="contact">
      <li>214 Franklin St #3B</li>
      <li>Brooklyn, NY 11222</li>
      <li>
        <svg viewBox="0 0 12 12" aria-hidden="true"><rect x="3" y="0.5" width="6" height="11" rx="1.2" fill="none" stroke="#e6e6e6" stroke-width="1.2"/><circle cx="6" cy="9.4" r="0.7" fill="#e6e6e6"/></svg>
        +330 2555-0141
      </li>
      <li>
        <svg viewBox="0 0 12 12" aria-hidden="true"><path d="M1 4.5C1 2.5 11 2.5 11 4.5L9.5 5.5 8.5 4.5H3.5L2.5 5.5Z" fill="#e6e6e6"/><rect x="2.5" y="6" width="7" height="5" rx="1" fill="#e6e6e6"/></svg>
        +330 2555-0187
      </li>
      <li>
        <svg viewBox="0 0 12 12" aria-hidden="true"><rect x="0.8" y="2.2" width="10.4" height="7.6" rx="1" fill="none" stroke="#e6e6e6" stroke-width="1.2"/><path d="M1 2.6 6 6.6 11 2.6" fill="none" stroke="#e6e6e6" stroke-width="1.2"/></svg>
        hello@lanternhill.com
      </li>
      <li>
        <svg viewBox="0 0 12 12" aria-hidden="true"><circle cx="6" cy="6" r="5" fill="none" stroke="#e6e6e6" stroke-width="1.1"/><ellipse cx="6" cy="6" rx="2.2" ry="5" fill="none" stroke="#e6e6e6" stroke-width="1"/><path d="M1 6H11" stroke="#e6e6e6" stroke-width="1"/></svg>
        www.lanternhill.com
      </li>
    </ul>
  </section>
</main>
</body>
</html>
```